New Branding Concept Healthcare Course Brochure

OBJECTIVE:
We need a new course brochure design to meet match our new branding colour scheme & concept as we are currently in the process of upgrading our website design. This A4 double sided brochure will briefly showcase a course on offer, in a clear, concise, professional and engaging way. This brochure will be in line with our new branding colour scheme and concept.
Our concept in monochrome with spashes & pops of colour (matching our logo colours) - see examples attached of imagery being used for social media currently as this somewhat reflects the concept we are working towards after, in terms of colour and look.

We are happy for you to be creative with formats. However, it must be able to include the same information as attached in "disability course brochure information". Have also attached some 'format examples' that we like - this is purely for ideas of paragraphing and formatting of information that other training providers are using, not for colour and graphic examples.

The final design will be used for promotional and adverting purposes to communicate information about a course to a prospective student in both print and soft copy form.

ORGANISATION OVERVIEW:
Verity Lane Institute (RTO.47381)
03 9417 2658
www.veritylaneinstitute.edu.au
admin@vli.edu.au
Head Office (Admin only): Level 5, 48 Marlowe Street, Ashgrove Park VIC 3196
3 modern & fully equipped training campuses across Melbourne: Ashgrove Park (Kestrel Road), Corrin Bay & Elmwood Heights.
We are a private registered training organisation based in Melbourne, Victoria, Australia specialising in only healthcare courses such as certificate III in pathology collection, Certificate IV in Disability, Certificate III in individual Support, Certificate IV in Aged Care & Certificate III in Health Services Assistance. We also offer professional development training workshops to corporate clients and the public such as first aid, cpr, medications, food saftey, manual handling and much more.

Target Market(s)

Prospective Healthcare Education Students

Font styles to use
Serif

Colors
f37122
fbed22
ffffff

Requirements
Must have
• MUST INCLUDE:
- ZPX Logo (attached)
- Our Logo (attached)
- Our slogan (Making you the future of healthcare)
- QR Code
- pops of colour must match our logo colours (see guide attached)
- contact details: website, social media buttons (instagram, facebook & twitter), phone number, email & our head office address.
- Must include relevant imagery (in this case disability or disability carer related, steer away from wheelchair images as it's used too much)
- must include information items (as per attached "disability brochure course information"

```html
<!DOCTYPE html>
<html lang="en">
<head>
<meta charset="utf-8">
<title>Certificate IV in Disability – Course Brochure</title>
<link href="https://fonts.googleapis.com/css2?family=Open+Sans:wght@400;600;700&family=Montserrat:wght@400;500;600&display=swap" rel="stylesheet">
<style>
:root{
  --orange:#f37122;
  --orange-soft:#f6a15d;
  --orange-deep:#e0571a;
  --yellow:#fbed22;
  --white:#ffffff;
  --ink:#4a4a4a;
  --muted:#777;
  --paper-tint:#f6f6f6;
  --stage:#e6e6e6;
  --rule:#d9d9d9;
}
*{box-sizing:border-box;margin:0;padding:0}
html,body{width:1200px;height:2400px;overflow:hidden;background:var(--stage)}
body{position:relative;font-family:"Open Sans",Arial,sans-serif;color:var(--ink)}
.spread{position:absolute;left:50px;width:1100px;height:853px;background:var(--white);box-shadow:0 6px 18px rgba(0,0,0,.18);overflow:hidden}
.spread--outside{top:250px}
.spread--inside{top:1200px}
.panel{position:absolute;top:0;width:550px;height:853px}
.panel--left{left:0}
.panel--right{left:550px}
.fold{position:absolute;left:550px;top:0;width:1px;height:853px;background:rgba(0,0,0,.08);z-index:5}
.heading{font-family:"Montserrat",sans-serif;font-weight:500;color:var(--orange);font-size:14px;letter-spacing:.2px;text-transform:uppercase}
.body-copy{font-size:10.5px;line-height:1.5;color:var(--ink);margin-top:5px}
.block{position:absolute;left:32px;right:32px}
.link{color:var(--orange);font-weight:700}
/* outside */
.photo{position:absolute}
.photo--carer-left{left:0;top:281px;width:550px;height:272px;background:linear-gradient(90deg,#fafafa 0%,#e2e2e2 45%,#b9b9b9 100%)}
.photo--carer-right{left:550px;top:281px;width:550px;height:420px;background:linear-gradient(160deg,#e9e9e9 0%,#a9a9a9 45%,#d4d4d4 100%)}
.band-art{position:absolute;left:0;top:540px;width:1100px;height:220px;z-index:2}
.contacts{position:absolute;left:30px;top:570px;width:240px;z-index:3;color:var(--white);font-size:10.5px;line-height:1.5}
.contacts li{list-style:none;display:flex;gap:8px;margin-bottom:6px}
.contacts svg{flex:none;margin-top:2px}
.apply{position:absolute;left:280px;top:572px;width:250px;z-index:3;color:var(--white);font-size:10.5px;line-height:1.45}
.apply h4{font-family:"Montserrat",sans-serif;font-weight:600;font-size:11px;text-transform:uppercase;margin-bottom:3px}
.apply .url{font-weight:700;margin-top:6px;display:flex;gap:6px;align-items:center}
.dot{display:inline-block;width:8px;height:8px;border-radius:50%;background:var(--yellow);flex:none}
.slogan{position:absolute;left:580px;top:585px;z-index:3;color:var(--white);font-family:"Montserrat",sans-serif}
.slogan .line1{font-size:25px;font-weight:400}
.slogan .line2{font-size:52px;font-weight:500;line-height:1.05;letter-spacing:1px}
.accred-badge{position:absolute;left:205px;top:770px;width:70px;height:46px;background:var(--orange-deep);opacity:.85}
.brand{position:absolute;left:550px;top:44px;width:550px;text-align:center}
.brand-mark{width:58px;height:58px;border-radius:50%;background:var(--orange);margin:0 auto 14px}
.brand-name{font-family:"Montserrat",sans-serif;font-weight:500;font-size:26px;color:var(--orange)}
.brand-rto{font-size:9px;color:var(--muted);margin-top:4px;letter-spacing:1px}
.cover-url{position:absolute;left:585px;top:782px;font-family:"Montserrat",sans-serif;font-size:16px;color:#333}
/* inside */
.panel--tint{background:var(--paper-tint)}
.info-band{position:absolute;left:0;top:234px;width:550px;height:314px;background:var(--orange);color:var(--white)}
.info-band .col{position:absolute;top:22px;font-size:10px;line-height:1.5}
.col--prospects{left:30px;width:230px}
.col--mode{left:280px;width:250px}
.info-band h3{font-family:"Montserrat",sans-serif;font-weight:500;font-size:14px;text-transform:uppercase}
.info-band h5{font-size:10px;font-weight:700;text-transform:uppercase;margin-top:12px}
.info-band .faint{color:#fde0c8}
.info-band ul{list-style:none}
.info-band li{display:flex;gap:6px}
.info-band li .dot{width:6px;height:6px;margin-top:5px}
.growth{display:flex;gap:12px;align-items:center;margin-bottom:18px}
.growth span{font-family:"Montserrat",sans-serif;font-size:17px;line-height:1.15}
.fees{display:flex;gap:30px;margin-top:8px;font-size:10.5px;line-height:1.45}
.fees li{list-style:none;display:flex;gap:6px}
.fees .dot{margin-top:4px;width:7px;height:7px}
.units{position:absolute;left:32px;top:192px;width:488px;border-collapse:collapse;font-size:9.5px}
.units th{background:var(--orange-soft);color:var(--white);text-align:left;font-weight:600;height:30px;padding-left:48px;font-size:10.5px}
.units th:last-child{padding-left:26px}
.units td{height:28px;border-bottom:1px solid var(--rule);padding-left:48px;color:#555}
.units td+td{padding-left:26px;border-left:1px solid var(--rule)}
.units .group td{background:var(--yellow);color:#444;font-weight:600;font-size:10.5px;padding-left:48px;border-left:none}
.units .code{width:145px}
</style>
</head>
<body>

<section class="spread spread--outside">
  <div class="fold"></div>

  <div class="panel panel--left">
    <div class="block" style="top:50px">
      <h2 class="heading">Opportunity for Recognition of Prior Learning (RPL)</h2>
      <p class="body-copy">Competencies gained through other formal study or experience may be acknowledged through a recognition process.</p>
    </div>
    <div class="block" style="top:128px">
      <h2 class="heading">Pathways</h2>
      <p class="body-copy">A possible training pathway for a participant completing this qualification could be any specialised area in the health sector or courses similar to the following: Certificate IV in Community Services; Certificate IV in Leisure and Health; Certificate IV in Ageing Support; Diploma of Community Services; Diploma of Nursing; Diploma of Leisure and Health</p>
    </div>
  </div>

  <div class="photo photo--carer-left" role="img" aria-label="Monochrome photo of a carer and client outdoors among trees"></div>
  <div class="photo photo--carer-right" role="img" aria-label="Monochrome photo of a support worker with an older woman by a large window"></div>

  <div class="block" style="top:300px;left:30px;width:250px;z-index:3">
    <h2 class="heading">Next Course Commencing</h2>
    <p class="body-copy">Regular intakes are available throughout the year. Please refer to our website at <span class="link">www.veritylaneinstitute.edu.au</span> for upcoming course dates.</p>
    <h2 class="heading" style="margin-top:20px">Questions?</h2>
    <p class="body-copy">Should you have any questions regarding Verity Lane Institute and the course, please contact one of our friendly team members on:</p>
  </div>

  <svg class="band-art" viewBox="0 0 1100 220" aria-hidden="true">
    <polygon points="0,13 1045,13 1000,178 0,178" fill="#f37122" opacity=".94"/>
    <polygon points="0,178 1085,178 1000,205 0,205" fill="#f6a15d"/>
  </svg>

  <ul class="contacts">
    <li><svg width="10" height="10" viewBox="0 0 10 10"><circle cx="5" cy="5" r="5" fill="#fbed22"/><path d="M3 2.5l1 1-.6.8c.4.8 1 1.4 1.8 1.8l.8-.6 1 1-.8 1C4.5 7.3 2.7 5.5 2.5 3.3z" fill="#f37122"/></svg><b>03 9417 2658</b></li>
    <li><svg width="10" height="10" viewBox="0 0 10 10"><circle cx="5" cy="5" r="5" fill="#fbed22"/><rect x="2.4" y="3.2" width="5.2" height="3.6" fill="none" stroke="#f37122" stroke-width=".8"/><path d="M2.4 3.2L5 5.3l2.6-2.1" fill="none" stroke="#f37122" stroke-width=".8"/></svg><span>admin@vli.edu.au<br>or visit us at:</span></li>
    <li><svg width="10" height="10" viewBox="0 0 10 10"><circle cx="5" cy="5" r="5" fill="#fbed22"/><path d="M5 2a2 2 0 0 1 2 2c0 1.5-2 4-2 4S3 5.5 3 4a2 2 0 0 1 2-2z" fill="#f37122"/></svg><span>Level 5, 48 Marlowe Street,<br>Ashgrove Park VIC 3196 (Head Office)</span></li>
  </ul>

  <div class="apply">
    <h4>How to apply online:</h4>
    <p>Complete an online application form<br>by clicking the below link</p>
    <p class="url"><span class="dot"></span>www.veritylaneinstitute.edu.au/apply</p>
  </div>

  <div class="slogan">
    <div class="line1">Making you the future of</div>
    <div class="line2">healthcare</div>
  </div>

  <div class="accred-badge" role="img" aria-label="Accreditation badge"></div>

  <div class="brand">
    <div class="brand-mark"></div>
    <div class="brand-name">Verity Lane Institute</div>
    <div class="brand-rto">RTO.47381</div>
  </div>

  <div class="cover-url">www.veritylaneinstitute.edu.au</div>
</section>

<section class="spread spread--inside">
  <div class="fold"></div>

  <div class="panel panel--left panel--tint">
    <div class="block" style="top:34px">
      <h2 class="heading">Course Overview</h2>
      <p class="body-copy">Start your rewarding career in disability with Verity Lane Institute and become a job-ready disability support worker (DSW).</p>
      <p class="body-copy">This qualification reflects the role of workers in a range of community settings and clients' homes, who provide training and support in a manner that empowers people with disabilities to achieve greater levels of independence, self-reliance, community participation and wellbeing, workers promote a person-centred approach and more.</p>
      <p class="body-copy">Verity Lane Institute is committed to providing an inclusive learning environment. Principles of access and equity for all students are applied in all programs. People with disabilities are encouraged to apply.</p>
    </div>

    <div class="info-band">
      <div class="col col--prospects">
        <h3>Job Prospects</h3>
        <p class="faint">Possible outcomes may include:</p>
        <ul class="faint">
          <li><span class="dot"></span>Community Worker</li>
          <li><span class="dot"></span>Disabilities Services Officer</li>
          <li><span class="dot"></span>Disability Support Worker</li>
        </ul>
        <h5>Delivery locations:</h5>
        <p class="faint">Ashgrove Park, Elmwood Heights &amp; Corrin Bay</p>
        <h5>Duration:</h5>
        <ul>
          <li><span class="dot"></span><b>22 weeks*</b></li>
        </ul>
        <p class="faint" style="padding-left:12px">of 1 day per week (9am-4.30pm)</p>
        <ul style="margin-top:4px">
          <li><span class="dot"></span><b>30 weeks*</b></li>
        </ul>
        <p class="faint" style="padding-left:12px">of 1 evening per week (5pm-9pm) + 3 Saturdays (9am-4.30pm)</p>
      </div>
      <div class="col col--mode">
        <div class="growth">
          <svg width="36" height="30" viewBox="0 0 36 30" aria-hidden="true">
            <rect x="2" y="18" width="6" height="10" fill="#fbed22"/>
            <rect x="11" y="13" width="6" height="15" fill="#fbed22"/>
            <rect x="20" y="8" width="6" height="20" fill="#fbed22"/>
            <rect x="29" y="2" width="6" height="26" fill="#fbed22"/>
            <line x1="0" y1="29" x2="36" y2="29" stroke="#fff" stroke-width="1.5"/>
          </svg>
          <span>Higher Than<br>Average Growth</span>
        </div>
        <p class="faint">Delivery location &amp; duration varies between intakes. Please refer to our website at <b style="color:#fff">www.veritylaneinstitute.edu.au</b> for upcoming course availability</p>
        <h5>Delivery mode:</h5>
        <p class="faint">Classroom &amp; blended/virtual learning</p>
        <h5>Practical experience and assessment:</h5>
        <p class="faint">Is undertaken throughout the course in the Verity Lane Institute simulated environment with trainers who are experts in their field and maintain currency in the industry.</p>
      </div>
    </div>

    <div class="block" style="top:572px">
      <h2 class="heading">Govt. Subsidised Training</h2>
      <p class="body-copy">This training is delivered with Victorian and Commonwealth Government funding under the Skills First Program and may impact your access to further government subsidised training.</p>
      <p class="body-copy">To find out if you are eligible, please contact us on 03 9417 2658 to discuss your circumstances or visit: <span class="link">https://www.veritylaneinstitute.edu.au/funded-courses.html</span></p>
    </div>

    <div class="block" style="top:700px">
      <h2 class="heading">Tuition Fees</h2>
      <p class="body-copy">The student tuition fees as published are subject to change given individual circumstances at enrolment.</p>
      <ul class="fees">
        <li><span class="dot"></span><span>Full Fee: <b>$3,200</b><br>Government Funded: <b>$250</b></span></li>
        <li><span class="dot"></span><span>Government Funded With Health Care Card,<br>Pensioner Concession Card or Vet Gold Card: <b>$250</b></span></li>
      </ul>
      <p class="body-copy" style="font-weight:700;font-size:10px">For detailed information regarding our course fees &amp; payment plans available please visit:<br><span class="link">www.veritylaneinstitute.edu.au/certificate-4-in-disability</span></p>
    </div>
  </div>

  <div class="panel panel--right">
    <div class="block" style="top:34px">
      <h2 class="heading">Practical Placement</h2>
      <p class="body-copy">Practical placement of 120 hours is a mandatory requirement of this course. Verity Lane Institute will organise on our students behalf.</p>
    </div>
    <div class="block" style="top:116px">
      <h2 class="heading">Units of Competency</h2>
      <p class="body-copy">16 units of competency are required to successfully complete this qualification. This includes 11 core units and 5 elective units, along with 120 hours of practical work placement.</p>
    </div>

    <table class="units">
      <thead><tr><th class="code">Unit Code</th><th>Units of Competency</th></tr></thead>
      <tbody>
        <tr class="group"><td colspan="2">Core Units</td></tr>
        <tr><td>CHCCCS015</td><td>Provide individualised Support</td></tr>
        <tr><td>CHCDIS002</td><td>Follow established person centred behaviour supports</td></tr>
        <tr><td>CHCDIS005</td><td>Develop and provide person centred service responses</td></tr>
        <tr><td>CHCDIS007</td><td>Facilitate the empowerment of people with disability</td></tr>
        <tr><td>CHCDIS008</td><td>Facilitate community participation and social inclusion</td></tr>
        <tr><td>CHCDIS009</td><td>Facilitate ongoing skills development using a person centred approach</td></tr>
        <tr><td>CHCDIS010</td><td>Provide person centred services to people with disability with complex needs</td></tr>
        <tr><td>CHCDIV001</td><td>Work with diverse people</td></tr>
        <tr><td>CHCLEG003</td><td>Manage legal and ethical compliance</td></tr>
        <tr><td>HLTAAP001</td><td>Recognise healthy body systems</td></tr>
        <tr><td>HLTWHS002</td><td>Follow safe work practices for direct client care</td></tr>
        <tr class="group"><td colspan="2">Elective units</td></tr>
        <tr><td>HLTFSE001</td><td>Follow basic food safety practices</td></tr>
        <tr><td>CHCCCS011</td><td>Meet personal support needs</td></tr>
        <tr><td>CHCLAH001</td><td>Work effectively with in the leisure and health industries</td></tr>
        <tr><td>HLTAID003</td><td>Provide first aid</td></tr>
        <tr><td>HLTINF001</td><td>Comply with infection prevention and control policies and procedures</td></tr>
      </tbody>
    </table>

    <div class="block" style="top:762px">
      <h2 class="heading">Opportunity for Credit Transfers (CT)</h2>
      <p class="body-copy">If students have already successfully completed unit/s of competency which are included within the qualification VLI offers, credit may be granted.</p>
    </div>
  </div>
</section>

</body>
</html>
```